Gestaltung von Honigetiketten
Zielgruppe
Ich bin ein Imker, der im eigenen Restaurant seinen Honig ausstellen und verkaufen möchte.
Aufgabenstellung
Ich möchte exklusive und edle Honigetiketten die auffallen. Bevorzugt mit den Farben Gold und Schwarz, siehe meinem bisher gesehenen Favoriten im Anhang.
Nur das Logo selbst (Baum) soll übernommen werden Farbe kann variieren, ebenso die Schrift ist variabel.
Auf die Vorderseite des Honigetiketts soll zu lesen sein:
- Deutscher Honig
- Sommertracht
- 500g
- Logo und Name
Auf der Rückseite des Honigetiketts soll zu finden sein:
- freies Feld für Stempel für Namen und Adresse des Abfüllers
- freies Feld für das Mindesthaltbarkeitsdatum

```html
<!DOCTYPE html>
<html lang="de">
<head>
<meta charset="utf-8">
<title>Honigetikett Sommertracht</title>
<link rel="stylesheet" href="https://fonts.googleapis.com/css2?family=Fira+Sans+Extra+Condensed:wght@400&family=Josefin+Sans:wght@300&family=Open+Sans:wght@400&display=swap">
<style>
  :root {
    --label-black: #0e0e0e;
    --band-black: #050505;
    --leaf-green: #66c400;
    --gold-text: #ddd08e;
    --gold-deep: #a8873a;
    --gold-light: #e8e0a4;
    --white: #ffffff;
    --faint: #2a2a2a;
  }
  * { margin: 0; padding: 0; box-sizing: border-box; }
  html, body { width: 732px; height: 1200px; overflow: hidden; background: var(--white); }
  .canvas { position: relative; width: 732px; height: 1200px; }

  /* Lid strip */
  .lid-strip {
    position: absolute; left: 309px; top: 260px; width: 131px; height: 440px;
    background: var(--band-black); overflow: hidden;
  }
  .comb-field {
    position: absolute; left: 0; width: 100%;
    background: linear-gradient(160deg, #1b170c 0%, #060606 55%, #1b170c 100%);
  }
  .comb-field--upper { top: 0; height: 150px; }
  .comb-field--lower { top: 302px; height: 138px; }
  .date-box {
    position: absolute; left: 21px; top: 13px; width: 94px; height: 43px;
    background: var(--white);
  }
  .date-box__text {
    position: absolute; left: 0; right: 0; top: 2px; text-align: center;
    font: 400 10px/1 "Fira Sans Extra Condensed", sans-serif; color: #000;
    transform: rotate(180deg); white-space: nowrap;
  }
  .brand-mark {
    position: absolute; border-radius: 50%;
    background: radial-gradient(circle at 45% 40%, var(--gold-light), var(--gold-deep));
  }
  .lid-strip .brand-mark { left: 19px; top: 161px; width: 93px; height: 93px; }
  .brand-name {
    position: absolute; left: 0; right: 0; text-align: center; white-space: nowrap;
    font: 400 14px/15.5px "Open Sans", sans-serif; color: var(--gold-text);
  }
  .lid-strip .brand-name { top: 264px; }

  /* Front label */
  .front-label {
    position: absolute; left: 87px; top: 700px; width: 572px; height: 240px;
    background: var(--label-black); overflow: hidden;
  }
  .front-label__band { position: absolute; left: 0; top: 0; width: 100%; height: 10px; background: var(--band-black); }
  .front-label__stripe { position: absolute; left: 0; top: 10px; width: 100%; height: 6px; background: var(--leaf-green); }
  .best-before {
    position: absolute; left: 420px; top: 1px;
    font: 400 8px/10px "Fira Sans Extra Condensed", sans-serif; color: var(--faint);
  }
  .address, .storage {
    position: absolute; white-space: nowrap;
    font: 400 13.5px/16.5px "Fira Sans Extra Condensed", sans-serif; color: var(--gold-text);
  }
  .address { left: 6px; top: 20px; }
  .storage { left: 415px; top: 23px; font-size: 13px; line-height: 15.5px; }
  .fill-amount {
    position: absolute; left: 415px; top: 88px; width: 70px; text-align: center;
    font: 400 14px/18px "Open Sans", sans-serif; color: var(--gold-text);
  }
  .front-label .brand-mark { left: 248px; top: 20px; width: 78px; height: 78px; }
  .front-label .brand-name { top: 104px; font-size: 16px; line-height: 16px; }
  .variety {
    position: absolute; left: 0; right: 0; top: 145px; text-align: center;
    font: 300 28px/1 "Josefin Sans", sans-serif; color: var(--leaf-green); letter-spacing: 0.5px;
  }
  .variety-rule { position: absolute; left: 210px; top: 179px; width: 150px; height: 2px; background: var(--leaf-green); }
  .origin {
    position: absolute; left: 0; right: 0; top: 185px; text-align: center;
    font: 300 16px/1 "Josefin Sans", sans-serif; color: var(--gold-text); letter-spacing: 0.5px;
  }
  .comb-gold {
    position: absolute; top: 92px; height: 148px;
    background: linear-gradient(120deg, var(--gold-deep), var(--gold-light) 50%, var(--gold-deep));
  }
  .comb-gold--left {
    left: 0; width: 228px;
    clip-path: polygon(0 0, 80px 0, 80px 39px, 144px 39px, 144px 78px, 207px 78px, 207px 116px, 228px 116px, 228px 148px, 0 148px);
  }
  .comb-gold--right {
    left: 343px; width: 229px;
    background: linear-gradient(60deg, var(--gold-deep), var(--gold-light) 60%, var(--gold-light));
    clip-path: polygon(148px 0, 229px 0, 229px 148px, 0 148px, 0 116px, 20px 116px, 20px 78px, 83px 78px, 83px 41px, 148px 41px);
  }
</style>
</head>
<body>
<main class="canvas">
  <section class="lid-strip">
    <div class="comb-field comb-field--upper" role="img" aria-label="Wabenmuster mit goldenen Linien auf Schwarz"></div>
    <div class="date-box"><p class="date-box__text">Mindestens haltbar bis</p></div>
    <div class="brand-mark" aria-hidden="true"></div>
    <p class="brand-name">Gasthof am Ahorn<br>Brunnsaal</p>
    <div class="comb-field comb-field--lower" role="img" aria-label="Wabenmuster mit goldenen Linien auf Schwarz"></div>
  </section>

  <section class="front-label">
    <div class="front-label__band"></div>
    <div class="front-label__stripe"></div>
    <p class="best-before">mindestens<br>haltbar bis:</p>
    <p class="address">Gasthaus Am Ahorn-Brunnsaal<br>Kastanienweg 14<br>91234 Feldbach-Mühlau<br>www.brunnsaal-ahornwirt.de</p>
    <p class="storage">Lagerhinweis:<br>Kühl, dunkel und trocken lagern.<br>Mehrwegglas:<br>Bitte zurück zum Imker</p>
    <p class="fill-amount">Füllmenge<br>500 g</p>
    <div class="comb-gold comb-gold--left" role="img" aria-label="Goldene Waben"></div>
    <div class="comb-gold comb-gold--right" role="img" aria-label="Goldene Waben"></div>
    <div class="brand-mark" aria-hidden="true"></div>
    <p class="brand-name">Gasthof am Ahorn<br>Brunnsaal</p>
    <h1 class="variety">Sommertracht</h1>
    <div class="variety-rule"></div>
    <p class="origin">Deutscher Honig</p>
  </section>
</main>
</body>
</html>
```